Wordpress Design for my Consulting Company

We want a WordPress site created for our new business. We have created a mock-up of the content we want on the site at https://marcusdellow.example-sites.com/website-5

We are not attached to any of the pictures and just put stock stuff from wix's editor, which we don't have rights to use outside of wix.

We are NOT looking to just port this site to WordPress, we are looking for some creative ways to display the content in a more professional artistic sense.

I have included several logo files and a text file with the colors and Fonts used in the logo. We are not looking to change the logo or the colors used in the logo.

The Schedule appointment links to a page that embeds a bookingnest.example.com calendar. https://bookingnest.example.com/marcus-dellow/brightvale

The final website domain will be enterprisebrightvale.example

Enterprise brightvale is a consulting company that works directly with the business owners and leaders of small businesses between 50-200 employees. We help companies make sure they have the right technology to meet their strategic goals. We are the anti-"Computer Guy" and we focus on business outcomes NOT cool technology gadgets.

The final design should communicate business growth and success.

Target Market(s)

Business Owners of companies with 50-200 employees

Coding

Coded - Design and coding required

Number of Pages Required

1 page

Font styles to use
Serif
Other font styles liked:
• Trajan Pro Bold, Open Sans

Requirements
Must have
• Should focus on consulting rather than technology.
• Should show the customer as the hero and we are just their guide.
• Must use the logo provided and the colors and fonts in the text file provided. Any other colors and fonts must be complementary.
• The design should scale for all devices computer, iPad, or phone
Should not have
• Should not focus on technology, we are the anti-"Computer Guy" and we focus on business outcomes NOT cool technology gadgets.

```html
<!DOCTYPE html>
<html lang="en">
<head>
<meta charset="UTF-8">
<title>Enterprise brightvale – The anti-"Computer Guy"</title>
<link rel="stylesheet" href="https://fonts.googleapis.com/css2?family=PT+Sans:wght@400;700&display=swap">
<style>
  :root {
    --page-bg: #ffffff;
    --ink: #111111;
    --tick-bg: #666666;
    --tick-mark: #ffffff;
    --accent: #ffa800;
    --band-dark: #1b1712;
    --band-mid: #4a3f33;
    --band-warm: #7a4b2a;
  }
  * { box-sizing: border-box; margin: 0; padding: 0; }
  html, body {
    width: 1200px;
    height: 550px;
    overflow: hidden;
    background: var(--page-bg);
  }
  .pain-section {
    position: relative;
    width: 1200px;
    height: 550px;
    font-family: "PT Sans", Tahoma, sans-serif;
    color: var(--ink);
  }
  .hero-band {
    position: absolute;
    top: 0; left: 0;
    width: 100%;
    height: 26px;
    background: linear-gradient(90deg, var(--band-dark) 0%, var(--band-mid) 45%, var(--band-dark) 70%, var(--band-warm) 100%);
  }
  .pain-heading {
    position: absolute;
    top: 28px;
    width: 100%;
    text-align: center;
    font-size: 26px;
    font-weight: 400;
    letter-spacing: 0.2px;
  }
  .pain-list {
    list-style: none;
  }
  .pain-item {
    position: absolute;
    width: 410px;
    font-size: 21.5px;
    line-height: 26.5px;
  }
  .tick-icon {
    display: inline-block;
    width: 44px;
    height: 44px;
    vertical-align: -4px;
    margin-right: 30px;
  }
  .col-left { left: 161px; }
  .col-right { left: 606px; }
  .row-1 { top: 112px; }
  .row-2 { top: 235px; }
  .row-3 { top: 358px; }
  .cta-button {
    position: absolute;
    left: 505px;
    top: 516px;
    width: 184px;
    height: 56px;
    border-radius: 28px;
    background: var(--accent);
    color: var(--ink);
    font-family: "PT Sans", Tahoma, sans-serif;
    font-size: 13px;
    text-align: center;
    line-height: 64px;
    text-decoration: none;
  }
</style>
</head>
<body>
<section class="pain-section">
  <div class="hero-band" role="img" aria-label="Photograph of an open road at dusk"></div>

  <h2 class="pain-heading">Are you tired of "Computer Guys" that...</h2>

  <svg width="0" height="0" style="position:absolute">
    <defs>
      <symbol id="tick" viewBox="0 0 44 44">
        <circle cx="22" cy="22" r="22" fill="var(--tick-bg)"/>
        <path d="M11 23 L18.5 30.5 L33 15" fill="none" stroke="var(--tick-mark)" stroke-width="6" stroke-linecap="round" stroke-linejoin="round"/>
      </symbol>
    </defs>
  </svg>

  <ul class="pain-list">
    <li class="pain-item col-left row-1"><svg class="tick-icon" aria-hidden="true"><use href="#tick"/></svg>Don't want to be involved in business strategy.</li>
    <li class="pain-item col-right row-1"><svg class="tick-icon" aria-hidden="true"><use href="#tick"/></svg>Give you the excuse, *You never asked.*</li>
    <li class="pain-item col-left row-2"><svg class="tick-icon" aria-hidden="true"><use href="#tick"/></svg>*Say No!* but do not give options on how to achieve your business outcome.</li>
    <li class="pain-item col-right row-2"><svg class="tick-icon" aria-hidden="true"><use href="#tick"/></svg>Recommend technology when a simple process or policy change would have the same effect.</li>
    <li class="pain-item col-left row-3"><svg class="tick-icon" aria-hidden="true"><use href="#tick"/></svg>Can't explain how a technology will create business value, but insist it is necessary.</li>
    <li class="pain-item col-right row-3"><svg class="tick-icon" aria-hidden="true"><use href="#tick"/></svg>Suggest expensive solutions that are just thrown away, soon after they are deployed.</li>
  </ul>

  <a class="cta-button" href="https://bookingnest.example.com/marcus-dellow/brightvale">Schedule Appointment</a>
</section>
</body>
</html>
```